Window Advertisment for Rentals Company

I own a property rental company in Cyprus and I am looking for an eye catching design to place in my window to attract passers by.

Please check the attachment for more details.

Ad size to be 309cm x 204cm landscape

The font of the logo is velocity

Target Market(s)

Property Owners

Industry/Entity Type

It Company

Requirements
Must have
• The colours from my logo and be eye catching and make passers by take notice

```html
<!DOCTYPE html>
<html lang="en">
<head>
<meta charset="utf-8">
<title>Sunward Stays Cyprus – Window Advertisement</title>
<link rel="stylesheet" href="https://fonts.googleapis.com/css2?family=Open+Sans:wght@700;800&display=swap">
<style>
  :root {
    --sun-yellow: #f9c31c;
    --brand-orange: #f0701f;
    --tile-orange: #f07a26;
    --heading-orange: #f26a21;
    --white: #ffffff;
    --sea-deep: #2f8aa0;
    --sea-light: #6bb8c3;
    --sand: #d8b88a;
    --sand-light: #e8d2ad;
    --sky: #4c9fe0;
  }
  * { margin: 0; padding: 0; box-sizing: border-box; }
  html, body { width: 1200px; height: 792px; overflow: hidden; background: var(--sun-yellow); }
  .poster {
    position: relative;
    width: 1200px;
    height: 792px;
    overflow: hidden;
    background: var(--sun-yellow);
    font-family: "Open Sans", Arial, sans-serif;
    font-weight: 700;
    color: var(--white);
  }
  .headline {
    position: absolute;
    top: 16px; left: 0; width: 100%;
    text-align: center;
    font-size: 32px;
    font-weight: 700;
    line-height: 48px;
    letter-spacing: 0.2px;
    text-transform: uppercase;
  }
  .headline .accent { color: var(--heading-orange); }
  .beach-scene {
    position: absolute;
    left: 0; top: 206px;
    width: 1200px; height: 462px;
    background: linear-gradient(180deg,
      var(--sea-deep) 0%, var(--sea-light) 38%, #9fcfcf 50%,
      var(--sand-light) 60%, var(--sand) 100%);
  }
  .property-photo {
    position: absolute;
    border: 6px solid var(--brand-orange);
    border-radius: 10px;
    box-shadow: 0 2px 6px rgba(0,0,0,0.35);
  }
  .property-photo.villa   { background: linear-gradient(180deg, var(--sky) 0%, #e9eef2 55%, #d9d2c5 100%); }
  .property-photo.garden  { background: linear-gradient(180deg, #3f6e3a 0%, #8aa86a 45%, #d9c49f 100%); }
  .property-photo.pool    { background: linear-gradient(180deg, var(--sky) 0%, #e8e4dc 45%, #2fa3d8 70%, #d8d4cc 100%); }
  .property-photo.interior{ background: linear-gradient(180deg, #f4f4f4 0%, #e6e3de 60%, #b89474 100%); }
  .property-photo.coast   { background: linear-gradient(180deg, #3e8fdc 0%, #d9ecf7 45%, #c8a679 75%, #b88d5c 100%); }
  .brand-name {
    position: absolute;
    left: 18px; top: 566px;
    width: 330px;
    display: flex; align-items: center; gap: 10px;
    font-size: 32px;
    font-weight: 800;
    color: var(--sun-yellow);
    text-transform: lowercase;
    line-height: 36px;
  }
  .brand-name .brand-dot {
    flex: none;
    width: 34px; height: 34px; border-radius: 50%;
    background: var(--sun-yellow);
  }
  .benefit {
    position: absolute;
    display: flex; align-items: center; justify-content: center;
    text-align: center;
    background: var(--tile-orange);
    border: 2px solid #f59a5a;
    border-radius: 10px;
    font-size: 16px;
    line-height: 22px;
    text-transform: uppercase;
    padding: 6px;
    box-shadow: 0 2px 5px rgba(0,0,0,0.25);
  }
  .contact {
    position: absolute;
    left: 19px; top: 684px;
    font-size: 21px;
    line-height: 33px;
    text-transform: uppercase;
  }
  .contact .value { color: var(--heading-orange); }
</style>
</head>
<body>
<main class="poster">
  <h1 class="headline">
    We are looking for <span class="accent">villas</span> and <span class="accent">apartments</span><br>
    to fulfill our growing demand of short term rentals
  </h1>

  <div class="beach-scene" role="img" aria-label="Sandy beach with rows of yellow parasols and turquoise sea"></div>

  <div class="property-photo villa"    style="left:15px;top:126px;width:177px;height:140px;transform:rotate(-4deg)" role="img" aria-label="White two-storey holiday villa"></div>
  <div class="property-photo garden"   style="left:193px;top:122px;width:168px;height:140px;transform:rotate(4deg)" role="img" aria-label="Garden terrace with sun loungers and palms"></div>
  <div class="property-photo pool"     style="left:362px;top:128px;width:163px;height:134px;transform:rotate(-2deg)" role="img" aria-label="Villa with private swimming pool"></div>
  <div class="property-photo villa"    style="left:527px;top:125px;width:168px;height:140px;transform:rotate(3deg)" role="img" aria-label="Cream villa with balcony"></div>
  <div class="property-photo interior" style="left:695px;top:121px;width:168px;height:140px;transform:rotate(-3deg)" role="img" aria-label="Bright apartment living room"></div>
  <div class="property-photo garden"   style="left:863px;top:121px;width:164px;height:140px;transform:rotate(3deg)" role="img" aria-label="Patio with loungers and palm trees"></div>
  <div class="property-photo coast"    style="left:1027px;top:125px;width:164px;height:136px;transform:rotate(-2deg)" role="img" aria-label="Coastal town view under blue sky"></div>

  <div class="brand-name" aria-label="Sunward Stays Cyprus"><span class="brand-dot"></span><span>sunward stays<br>cyprus</span></div>

  <div class="benefit" style="left:360px;top:575px;width:158px;height:130px;transform:rotate(-3deg)">Low<br>commissions</div>
  <div class="benefit" style="left:524px;top:572px;width:166px;height:136px;transform:rotate(4deg)">Quick<br>payouts</div>
  <div class="benefit" style="left:693px;top:575px;width:164px;height:130px;transform:rotate(-2deg)">Free<br>advertising</div>
  <div class="benefit" style="left:861px;top:572px;width:166px;height:136px;transform:rotate(4deg)">Connect<br>with over<br>35 leading<br>websites</div>
  <div class="benefit" style="left:1032px;top:572px;width:160px;height:132px;transform:rotate(-3deg)">Be seen by<br>100+ million<br>travelers<br>per month</div>

  <div class="contact">
    <div>Contact:</div>
    <div>Web: <span class="value">www.sunwardstays-example.com</span></div>
    <div>Tel: <span class="value">23 555014</span></div>
  </div>
</main>
</body>
</html>
```